CEO Survey Report Landing Page - lead response

Looking for responsive design landing page done in modern elegant style that will appeal to the top executive (CEO) of big businesses. This page should collect first name, last name, business email and have download button. we require source file in both adobe photoshop psd and indesign (idd).

Example of landing page: https://blog.plintrova.com/post/503817264915/how-to-design-an-optimized-ebook-landing-page (see attachments for more examples)

Target Market(s)

CEO - top executive of US business between 100 million to 1 billion a year in revenue

Number of Pages Required

1 page

Font styles to use
Sans Serif

Colors
0692cd
ffffff
f78f20
9bcb3b

Requirements
Must have
• place the copy text given in the doc on the page. we are focusing on 1. meaning of copy text being powerful and easy to understand. 2. a way to highlight the 3 numeric values with text . 3. clear call to action.
Nice to have
• idea 1. see the 3 numbers with a graphic. consider for example like put each number in a circle with label below.
• optional idea 2. perhaps consider an elegant business info-graphic look
• optional idea 3. as an option consider screened gradient color in blue /green or photo with translucent layer - behind make white / light gray main area where have copy etc.
Should not have
• do NOT make this look like a regular website. see the plintrova link and sample reference of landing page designs. it should be a landing page with clear easy elegant form with a lot of clear space.
• have cluttered looks. photo images of people in the foreground etc that distracts is bad. a screened back photo in the background is fine.

```html
<!DOCTYPE html>
<html lang="en">
<head>
<meta charset="utf-8">
<title>CEO Survey – Landing Page</title>
<link rel="stylesheet" href="https://fonts.googleapis.com/css2?family=Montserrat:wght@400;500;600&family=Roboto+Slab:wght@400&family=Arimo:wght@400&display=swap">
<style>
  :root{
    --board-top:#eef7ff;
    --board-bottom:#2e98fb;
    --brand-blue:#1e8ff5;
    --accent-blue:#3aa0f7;
    --band-blue:#1684f8;
    --ink:#3a3a3a;
    --muted:#555;
    --white:#ffffff;
    --black:#000000;
    --panel-light:#f4f4f4;
    --bar-green:#8cbf1f;
    --bar-sky:#6cc3e0;
    --bar-yellow:#f0d21a;
    --bar-orange:#f26a10;
    --bar-purple:#6b1f6b;
    --bar-blue:#1a8fe0;
  }
  *{box-sizing:border-box;margin:0;padding:0}
  html,body{width:714px;height:1200px;overflow:hidden}
  body{
    background:linear-gradient(160deg,var(--board-top) 0%,#9fd2fb 45%,var(--board-bottom) 100%);
    font-family:"Montserrat",sans-serif;
    position:relative;
  }
  .page{position:absolute;left:45px;width:625px;overflow:hidden}
  .page--form{top:53px;height:406px}
  .page--report{top:506px;height:649px}

  .hero{position:absolute;left:0;top:0;width:625px}
  .hero__photo{position:absolute;inset:0}
  .page--form .hero{height:374px}
  .page--form .hero__photo{
    background:radial-gradient(ellipse at 72% 55%,#6b5a45 0%,#3b3430 45%,#1f1c1b 100%);
  }
  .page--report .hero{height:326px}
  .page--report .hero__photo{
    background:radial-gradient(ellipse at 65% 45%,#3b4255 0%,#262b39 45%,#101218 100%);
  }

  .hero__title{position:absolute;left:44px;font-weight:400;line-height:1;white-space:nowrap}
  .page--form .hero__title{top:125px;font-size:34px;font-family:"Montserrat",sans-serif;color:var(--accent-blue)}
  .page--report .hero__title{top:96px;font-size:32px;font-family:"Roboto Slab",Georgia,serif;color:var(--brand-blue)}

  .hero__intro{position:absolute;left:45px;top:168px;color:var(--white);
    font-family:"Arimo",sans-serif;font-size:6.6px;line-height:14px;white-space:nowrap}

  .lead-form__field{position:absolute;left:45px;width:198px;height:21px;background:var(--white);
    border-radius:2px;font-family:"Arimo",sans-serif;font-size:7px;color:#333;padding-left:8px;line-height:21px}
  .lead-form__button{position:absolute;left:45px;top:281px;width:64px;height:21px;background:var(--brand-blue);
    color:var(--white);font-size:7.5px;font-weight:500;text-align:center;line-height:21px;border-radius:2px}

  .footer{position:absolute;left:0;bottom:0;width:625px;height:32px;background:var(--black);
    color:var(--white);font-family:"Arimo",sans-serif;font-size:6.5px;text-align:center;line-height:32px}
  .footer__code{position:absolute;right:30px;top:7px;font-size:6px}

  .hero__headline{position:absolute;left:44px;top:145px;color:var(--accent-blue);font-size:12px;font-weight:500;white-space:nowrap}
  .hero__subhead{position:absolute;left:45px;top:170px;color:var(--white);font-size:9.7px;font-weight:500;white-space:nowrap}
  .hero__kicker{position:absolute;left:45px;top:191px;color:var(--white);font-size:7px;font-weight:500;white-space:nowrap}
  .hero__list{position:absolute;left:44px;top:217px;list-style:none}
  .hero__list li{color:var(--white);font-size:8px;font-weight:500;height:20px;display:flex;align-items:center;white-space:nowrap}
  .hero__list svg{margin-right:10px}
  .hero__list em{font-style:normal;color:var(--accent-blue)}

  .cta-band{position:absolute;left:0;top:326px;width:625px;height:69px;background:var(--band-blue)}
  .cta-band__text{position:absolute;left:64px;top:0;line-height:69px;color:var(--white);font-size:10.8px;font-weight:500;white-space:nowrap}
  .cta-band__button{position:absolute;left:427px;top:22px;width:142px;height:25px;border:1px solid var(--white);
    border-radius:2px;color:var(--white);font-size:7.5px;font-weight:500;text-align:center;line-height:23px;white-space:nowrap}

  .concerns{position:absolute;left:0;top:395px;width:625px;height:222px;background:var(--panel-light)}
  .concerns__title{position:absolute;top:22px;width:100%;text-align:center;font-size:13.5px;font-weight:500;color:var(--ink)}
  .concerns__row{position:absolute;left:106px;height:8px;width:450px}
  .concerns__label{position:absolute;left:0;top:0;font-size:6px;font-weight:500;color:var(--muted);line-height:8px;white-space:nowrap}
  .concerns__bar{position:absolute;left:157px;top:2px;height:5px;border-radius:3px}
  .concerns__value{position:absolute;top:0;font-size:6px;color:var(--muted);line-height:8px}
  .concerns__accent{position:absolute;left:412px;top:80px;width:110px;height:120px;
    background:radial-gradient(ellipse at 35% 30%,rgba(120,120,120,0.22) 0%,rgba(120,120,120,0.08) 45%,rgba(120,120,120,0) 70%)}
</style>
</head>
<body>

<section class="page page--form">
  <div class="hero">
    <div class="hero__photo" role="img" aria-label="Dimmed background photo of a hand tapping a satisfaction rating with check mark and five stars"></div>
    <h1 class="hero__title">CEO Survey</h1>
    <p class="hero__intro">Sed ut perspiciatis unde omnis iste natus error sit voluptatem accusan<br>laudantium, totam ab illo inventore veritatis explicabo.</p>
    <div class="lead-form__field" style="top:203px">First Name :</div>
    <div class="lead-form__field" style="top:226px">Last Name :</div>
    <div class="lead-form__field" style="top:251px">Business Email :</div>
    <div class="lead-form__button">DOWNLOAD</div>
  </div>
  <footer class="footer">© Copyright-2018 CEO Survey. All rights reserved.<span class="footer__code">C2</span></footer>
</section>

<section class="page page--report">
  <div class="hero">
    <div class="hero__photo" role="img" aria-label="Dimmed background photo of a businessman selecting a check box on a rating scale"></div>
    <h1 class="hero__title">CEO Survey</h1>
    <h2 class="hero__headline">JOHN ACHIEVE YOUR OBJECTIVES EASIER</h2>
    <p class="hero__subhead">SEE WHAT OTHER CEOS ARE SAYING ABOUT CLOUD</p>
    <p class="hero__kicker">GET THE 2018 CEO CLOUD SURVEY</p>
    <ul class="hero__list">
      <li><svg width="7" height="6" viewBox="0 0 7 6"><path d="M0.5 3 L2.6 5 L6.5 0.8" fill="none" stroke="#1e8ff5" stroke-width="1.5"/></svg>5000 CEOs Of US Mid-Sized Companies</li>
      <li><svg width="7" height="6" viewBox="0 0 7 6"><path d="M0.5 3 L2.6 5 L6.5 0.8" fill="none" stroke="#1e8ff5" stroke-width="1.5"/></svg>6 Things To Know |&nbsp;<em>Cloud Pitfalls | Areas To Watch Out</em></li>
      <li><svg width="7" height="6" viewBox="0 0 7 6"><path d="M0.5 3 L2.6 5 L6.5 0.8" fill="none" stroke="#1e8ff5" stroke-width="1.5"/></svg>6 Recommendations</li>
    </ul>
  </div>

  <div class="cta-band">
    <p class="cta-band__text">A QUICK 10 MINUTE READ TO SUCCEED BETTER WITH CLOUD</p>
    <div class="cta-band__button">DOWNLOAD THE REPORT NOW!</div>
  </div>

  <div class="concerns">
    <h3 class="concerns__title">CLOUD CONCERNS</h3>
    <div class="concerns__row" style="top:70px"><span class="concerns__label">TAX ON EXECUTIVE TIME TO OVERSEE</span><span class="concerns__bar" style="width:152px;background:var(--bar-green)"></span><span class="concerns__value" style="left:316px">50%</span></div>
    <div class="concerns__row" style="top:89px"><span class="concerns__label">WORRY ABOUT TEAM EXECUTION</span><span class="concerns__bar" style="width:186px;background:var(--bar-sky)"></span><span class="concerns__value" style="left:350px">65%</span></div>
    <div class="concerns__row" style="top:108px"><span class="concerns__label">COST</span><span class="concerns__bar" style="width:210px;background:var(--bar-yellow)"></span><span class="concerns__value" style="left:374px">70%</span></div>
    <div class="concerns__row" style="top:127px"><span class="concerns__label">SECURITY</span><span class="concerns__bar" style="width:237px;background:var(--bar-orange)"></span><span class="concerns__value" style="left:401px">81%</span></div>
    <div class="concerns__row" style="top:146px"><span class="concerns__label">KEEP PACE WITH CLOUD EVOLUTION</span><span class="concerns__bar" style="width:170px;background:var(--bar-purple)"></span><span class="concerns__value" style="left:334px">57%</span></div>
    <div class="concerns__row" style="top:165px"><span class="concerns__label">RETENTION OF CLOUD TALENT</span><span class="concerns__bar" style="width:112px;background:var(--bar-blue)"></span><span class="concerns__value" style="left:276px">20%</span></div>
    <div class="concerns__accent" role="img" aria-label="Magnifying glass illustration over the chart"></div>
  </div>

  <footer class="footer">© Copyright-2018 CEO Survey. All rights reserved.<span class="footer__code">C2</span></footer>
</section>

</body>
</html>
```